"Made in Chicago" Baby Shower Invitation

I need a design for a baby shower invitation with the headline and theme of "Made in Chicago". The design should incorporate the colors/design of the Chicago flag. I have attached an image of the flag for your reference. The design should be sized 5-1/2 wide x 8-1/2 long. I want to be able to print two to a page on a standard 8-1/2 X 11" piece of (nice quality) paper on a standard home printer.
Copy:
Made in Chicago Baby Shower
For: Mirela & Gordon
Date: Saturday, April 5, 2014
Time: 7:00 p.m.
Place: 42 West Halloway Ave, 5B
RSVP by April 1 to Dana Whitmoor/312-555-0193

Hello Designers - I corrected the size requirements of the invitation (bad math before) and added a few more notes of preference. Looking for a design that is more clean and graphic and less traditional, soft baby shower look. Thank you!

Friends & family of the 20-sometthing, urban professional couple who are having a baby.

Baby

Must have
• Chicago flag colors and/or image, the words "made in Chicago", and the (revised) size indicated.
Should not have
• Anything inappropriate or offensive to grandmother of said couple.

```html
<!DOCTYPE html>
<html lang="en">
<head>
<meta charset="utf-8">
<title>Made in Chicago Baby Shower Invitation</title>
<link rel="stylesheet" href="https://fonts.googleapis.com/css2?family=Quicksand:wght@400;500;600&family=Yanone+Kaffeesatz:wght@400;600;700&family=Gochi+Hand&display=swap">
<style>
  :root {
    --frame-dark: #4d7386;
    --frame-light: #8fbdd0;
    --paper: #ffffff;
    --ink-teal: #3e6677;
    --ink-red: #f0461f;
    --ink-red-dark: #b9321a;
    --ink-black: #1f1f1f;
    --scroll-light: #e6ddc9;
    --scroll-mid: #c9bb9d;
    --scroll-dark: #a89878;
  }
  html, body {
    margin: 0;
    padding: 0;
    overflow: hidden;
    background: var(--paper);
  }
  .invitation {
    position: relative;
    width: 776px;
    height: 1200px;
    box-sizing: border-box;
    background: var(--frame-dark);
    padding: 12px;
    overflow: hidden;
  }
  .invitation__inner {
    position: relative;
    width: 100%;
    height: 100%;
    box-sizing: border-box;
    background: var(--frame-light);
    padding: 10px;
  }
  .invitation__card {
    position: relative;
    width: 100%;
    height: 100%;
    background: var(--paper);
  }
  .centered {
    position: absolute;
    left: 0;
    right: 0;
    text-align: center;
    margin: 0;
  }
  .kicker {
    top: 38px;
    font-family: "Quicksand", sans-serif;
    font-weight: 500;
    font-size: 29px;
    color: var(--ink-teal);
  }
  .headline {
    top: 72px;
    font-family: "Quicksand", sans-serif;
    font-weight: 500;
    font-size: 54px;
    letter-spacing: 1px;
    color: var(--ink-teal);
  }
  .banner {
    position: absolute;
    left: 70px;
    top: 146px;
    width: 612px;
    height: 70px;
  }
  .banner__text {
    top: 158px;
    font-family: "Gochi Hand", cursive;
    font-size: 25px;
    color: var(--paper);
    letter-spacing: 1px;
  }
  .couple {
    top: 268px;
    font-family: "Yanone Kaffeesatz", sans-serif;
    font-weight: 700;
    font-variant: small-caps;
    font-size: 140px;
    line-height: 1;
    color: var(--ink-teal);
    letter-spacing: 1px;
  }
  .day {
    position: absolute;
    left: 40px;
    top: 466px;
    margin: 0;
    font-family: "Gochi Hand", cursive;
    font-size: 52px;
    color: var(--ink-black);
    letter-spacing: 1px;
  }
  .day-rule {
    position: absolute;
    left: 40px;
    top: 540px;
    width: 290px;
    border-top: 3px dotted var(--ink-red);
  }
  .date {
    position: absolute;
    left: 40px;
    top: 552px;
    margin: 0;
    font-family: "Quicksand", sans-serif;
    font-weight: 400;
    font-size: 72px;
    color: var(--ink-red);
  }
  .time-scroll {
    position: absolute;
    left: 350px;
    top: 466px;
    width: 340px;
    height: 120px;
  }
  .time {
    position: absolute;
    left: 370px;
    top: 484px;
    width: 300px;
    margin: 0;
    text-align: center;
    font-family: "Quicksand", sans-serif;
    font-weight: 500;
    font-size: 44px;
    color: var(--paper);
  }
  .place {
    top: 664px;
    font-family: "Quicksand", sans-serif;
    font-weight: 500;
    font-size: 33px;
    color: var(--ink-black);
  }
  .rule {
    position: absolute;
    left: 72px;
    right: 72px;
    top: 724px;
    border-top: 3px solid var(--ink-red);
  }
  .rsvp {
    top: 752px;
    font-family: "Yanone Kaffeesatz", sans-serif;
    font-weight: 400;
    font-variant: small-caps;
    font-size: 40px;
    letter-spacing: 1.5px;
    color: var(--ink-teal);
  }
  .bow {
    position: absolute;
    left: 232px;
    top: 840px;
    width: 264px;
    height: 230px;
    border-radius: 12px;
    background: radial-gradient(circle at 50% 40%, #dbe7ec 0%, #eef4f6 60%, var(--paper) 100%);
  }
</style>
</head>
<body>
<main class="invitation">
  <div class="invitation__inner">
    <section class="invitation__card">
      <p class="centered kicker">Made in Chicago</p>
      <h1 class="centered headline">BABY SHOWER</h1>

      <svg class="banner" viewBox="0 0 612 70" aria-hidden="true">
        <polygon points="0,18 46,18 46,62 0,62 14,40" fill="var(--ink-red-dark)"/>
        <polygon points="612,18 566,18 566,62 612,62 598,40" fill="var(--ink-red-dark)"/>
        <polygon points="30,8 582,8 582,54 30,54" fill="var(--ink-red)"/>
        <polygon points="30,54 46,54 46,62" fill="#7d2210"/>
        <polygon points="582,54 566,54 566,62" fill="#7d2210"/>
      </svg>
      <p class="centered banner__text">mommy &amp; daddy to be</p>

      <h2 class="centered couple">Mirela &amp; Gordon</h2>

      <p class="day">SATURDAY</p>
      <div class="day-rule"></div>
      <p class="date">April 5</p>

      <svg class="time-scroll" viewBox="0 0 340 120" aria-hidden="true">
        <defs>
          <linearGradient id="scrollFace" x1="0" y1="0" x2="0" y2="1">
            <stop offset="0" stop-color="var(--scroll-light)"/>
            <stop offset="1" stop-color="var(--scroll-mid)"/>
          </linearGradient>
        </defs>
        <path d="M4,20 C60,0 140,40 200,24 C250,10 300,10 336,26 L336,96 C300,80 250,80 200,94 C140,110 60,70 4,90 Z" fill="url(#scrollFace)"/>
        <path d="M4,20 C-6,30 -6,82 4,90 C14,84 18,30 4,20 Z" fill="var(--scroll-dark)"/>
        <path d="M336,26 C346,40 346,88 336,96 C326,88 326,38 336,26 Z" fill="var(--scroll-dark)"/>
      </svg>
      <p class="time">7:00 pm</p>

      <p class="centered place">Place: 42 West Halloway Ave, 5B</p>
      <div class="rule"></div>
      <p class="centered rsvp">RSVP by April 1 to Dana Whitmoor/312-555-0193</p>

      <div class="bow" role="img" aria-label="Hand-drawn teal ribbon bow with curling tails"></div>
    </section>
  </div>
</main>
</body>
</html>
```